Aged Care Consultancy Business needs a business card design

I need a two sided business card - I want it clean and professional. Surprise me

Target Market(s)

middle aged and ageing victorians

Industry/Entity Type

Health Care

Contact Information for Business Card

Text to be included

Logo
Aged Care Consulting Services
Professional, Reliable, Affordable

Tovan Brelsick
Director
0427 31 64 92 (larger)
1300 73 29 41
tovan@wadolire.com.au
www.wadolcare.com.au
Facebook (details TBA)

include little icons beside the contact info:

- Envelope = email
- Phone = phone
- Globe = website

Font styles to use
Serif
Sans Serif

Requirements
Must have
• look proffesional and clean

```html
<!DOCTYPE html>
<html lang="en">
<head>
<meta charset="utf-8">
<title>wadol care – business card</title>
<link rel="stylesheet" href="https://fonts.googleapis.com/css2?family=Bebas+Neue&family=Lato:wght@400;700;900&display=swap">
<style>
  :root {
    --navy: #1d4580;
    --orange: #e8952a;
    --ink: #3c3c3c;
    --rule: #9a9a9a;
    --paper: #ffffff;
    --backdrop: #e9e7e4;
  }
  * { margin: 0; padding: 0; box-sizing: border-box; }
  html, body { width: 1200px; height: 960px; overflow: hidden; }
  body {
    background: var(--backdrop);
    position: relative;
    font-family: "Lato", Arial, sans-serif;
  }
  .card {
    position: absolute;
    left: 250px;
    width: 704px;
    height: 400px;
    box-shadow: 0 3px 8px rgba(0,0,0,0.18);
  }
  .card--front { top: 50px; background: var(--paper); }
  .card--back  { top: 510px; background: var(--navy); }

  .brand {
    position: absolute;
    left: 38px;
    top: 222px;
    width: 300px;
    height: 60px;
    display: flex;
    align-items: center;
    justify-content: center;
    gap: 10px;
  }
  .brand__dot {
    width: 22px; height: 22px;
    border-radius: 50%;
    background: var(--orange);
    flex: none;
  }
  .brand__name {
    font-weight: 900;
    font-size: 44px;
    line-height: 60px;
    letter-spacing: 0.5px;
    color: var(--navy);
    white-space: nowrap;
  }
  .divider {
    position: absolute;
    left: 352px;
    top: 103px;
    width: 1.5px;
    height: 194px;
    background: var(--rule);
  }
  .person {
    position: absolute;
    left: 395px;
    top: 100px;
  }
  .person__name {
    font-family: "Bebas Neue", "Arial Narrow", sans-serif;
    font-size: 34px;
    line-height: 34px;
    color: var(--navy);
    letter-spacing: 0.3px;
  }
  .person__role {
    font-size: 19px;
    line-height: 24px;
    color: var(--orange);
  }
  .person__mobile {
    font-size: 21px;
    line-height: 25px;
    color: var(--navy);
    letter-spacing: 0.3px;
  }
  .contacts {
    position: absolute;
    left: 397px;
    top: 209px;
    list-style: none;
  }
  .contacts__item {
    display: flex;
    align-items: center;
    gap: 6px;
    font-size: 17px;
    line-height: 22.5px;
    color: var(--ink);
  }
  .contacts__icon { width: 17px; height: 17px; flex: none; }

  .back-brand {
    position: absolute;
    left: 0;
    right: 0;
    top: 230px;
    text-align: center;
    font-weight: 900;
    font-size: 82px;
    line-height: 90px;
    color: var(--paper);
    letter-spacing: 1px;
  }
</style>
</head>
<body>

<section class="card card--front">
  <div class="brand">
    <span class="brand__dot"></span>
    <span class="brand__name">wadol care</span>
  </div>

  <div class="divider"></div>

  <div class="person">
    <div class="person__name">Tovan Brelsick</div>
    <div class="person__role">Director</div>
    <div class="person__mobile">0427 31 64 92</div>
  </div>

  <ul class="contacts">
    <li class="contacts__item">
      <svg class="contacts__icon" viewBox="0 0 17 17" aria-hidden="true">
        <rect width="17" height="17" rx="3" fill="var(--navy)"/>
        <path d="M6 3.5 L7.6 6 L6.6 7.2 Q7.6 9.6 9.8 10.6 L11 9.6 L13.3 11.2 L12.3 13.3 Q6.5 13 4 5 Z" fill="#fff"/>
      </svg>
      <span>1300 73 29 41</span>
    </li>
    <li class="contacts__item">
      <svg class="contacts__icon" viewBox="0 0 17 17" aria-hidden="true">
        <rect width="17" height="17" rx="3" fill="var(--navy)"/>
        <rect x="3" y="4.5" width="11" height="8" fill="none" stroke="#fff" stroke-width="1.3"/>
        <path d="M3 4.5 L8.5 9 L14 4.5" fill="none" stroke="#fff" stroke-width="1.3"/>
      </svg>
      <span>tovan@wadolire.com.au</span>
    </li>
    <li class="contacts__item">
      <svg class="contacts__icon" viewBox="0 0 17 17" aria-hidden="true">
        <rect width="17" height="17" rx="3" fill="var(--navy)"/>
        <circle cx="8.5" cy="8.5" r="5.5" fill="none" stroke="#fff" stroke-width="1.2"/>
        <ellipse cx="8.5" cy="8.5" rx="2.4" ry="5.5" fill="none" stroke="#fff" stroke-width="1"/>
        <path d="M3 8.5 H14 M4 5.8 H13 M4 11.2 H13" stroke="#fff" stroke-width="1"/>
      </svg>
      <span>www.wadolcare.com.au</span>
    </li>
    <li class="contacts__item">
      <svg class="contacts__icon" viewBox="0 0 17 17" aria-hidden="true">
        <rect width="17" height="17" rx="3" fill="var(--navy)"/>
      </svg>
      <span>linkup.com.au/wadolcare</span>
    </li>
  </ul>
</section>

<section class="card card--back">
  <div class="back-brand">wadol care</div>
</section>

</body>
</html>
```